TAVRO Capital Group LLC a High Risk Big Rewards company for Rich Young Entrepreneurs

We would like a very modern, powerful in the eyes of our customers, modern, minimalist feel, financial gain. this business card is for young Rich entrepreneurs who want to invest money into High Risk, Big Rewards Businesses. The card Should sell the business!! let your creativity go Wild! I pick most of the designers for this project because of your BOLD Designs, I would like this card to be Bold, Modern, Minimalist, use as many effects in your graphic Artist Mind, Do not let the Financial sound of this business to make you think Conservative that's the last thing we are! if you have a lot of money and you want to play a risky market call US
Updates

Project Deadline Extended
Reason: have not received, enough designs to choose 1st and second place, sure I have received over 100 designs but it seems most designers are submitting every card they have ever made before and calling it mine, please we are looking for fresh ideas please!

Target Market(s)

Private Risky Investors

Industry/Entity Type

Financial

Contact Information for Business Card

powerful in the eyes of our customers,modern, minimalist feel

Font styles to use
Other font styles liked:
• Modern feeling fonts

Requirements
Must have
• The Company Name is TAVRO Capital Group LLC and it must be on the CARD
• My Name, title, Cell , email
• Delvin Ashcroft G.E.D.
• Managing Member
• 555.038.6195
• delvin@tavrocapitalgroup.example
Nice to have
• try a black thick plastic card with round corners with Delvin Ashcroft GED (make sure GED is smaller than name) just on one side of the card, and my phone number with out the icons and email on the other side, this card should look like a exclusive credit card or exclusive VIP card, something you would never loose

```html
<!DOCTYPE html>
<html lang="en">
<head>
<meta charset="utf-8">
<title>TAVRO Capital Group LLC — Business Card</title>
<link rel="stylesheet" href="https://fonts.googleapis.com/css2?family=Saira:wght@300;400&family=Roboto:wght@400;700&family=Roboto+Mono:wght@400&display=swap">
<style>
  :root {
    --page: #ffffff;
    --card: #171717;
    --card-edge: #3a3a3a;
    --ink: #ffffff;
    --rule: #9a9a9a;
    --blue-light: #0a8cec;
    --blue-mid: #1f5fd0;
    --blue-deep: #2a2a9e;
    --blue-night: #271f6e;
  }
  html, body {
    margin: 0;
    padding: 0;
    width: 1053px;
    height: 1200px;
    overflow: hidden;
    background: var(--page);
  }
  .sheet {
    position: relative;
    width: 1053px;
    height: 1200px;
  }
  .card {
    position: absolute;
    left: 208px;
    width: 688px;
    height: 380px;
    background: var(--card);
    box-shadow: 0 0 0 1px var(--card-edge);
    overflow: hidden;
    color: var(--ink);
  }
  .card--front { top: 206px; }
  .card--back  { top: 614px; }

  /* Soft colour field standing in for the angled band decoration */
  .glow {
    position: absolute;
    pointer-events: none;
  }
  .glow--front {
    right: 0;
    bottom: 0;
    width: 380px;
    height: 230px;
    background:
      radial-gradient(ellipse 70% 80% at 85% 70%, rgba(31, 95, 208, 0.85) 0%, rgba(42, 42, 158, 0.45) 45%, rgba(23, 23, 23, 0) 100%);
  }
  .glow--back {
    right: 0;
    top: 0;
    width: 300px;
    height: 380px;
    background:
      radial-gradient(ellipse 80% 60% at 75% 35%, rgba(10, 140, 236, 0.8) 0%, rgba(42, 42, 158, 0.55) 45%, rgba(39, 31, 110, 0.25) 70%, rgba(23, 23, 23, 0) 100%);
  }

  /* Front */
  .brand-mark {
    position: absolute;
    left: 204px;
    top: 180px;
    width: 40px;
    height: 40px;
    background: var(--blue-mid);
  }
  .brand-rule {
    position: absolute;
    left: 66px;
    top: 239px;
    width: 316px;
    height: 1px;
    background: var(--rule);
  }
  .brand-name {
    position: absolute;
    left: 66px;
    width: 316px;
    top: 242px;
    margin: 0;
    font-family: "Saira", sans-serif;
    font-weight: 300;
    font-size: 29px;
    line-height: 36px;
    text-align: center;
    white-space: nowrap;
  }
  .role {
    position: absolute;
    left: 66px;
    width: 316px;
    top: 291px;
    margin: 0;
    font-family: "Roboto Mono", monospace;
    font-size: 13.5px;
    line-height: 18px;
    text-align: center;
    letter-spacing: 0.3px;
  }

  /* Back */
  .pitch {
    position: absolute;
    left: 59px;
    top: 100px;
    margin: 0;
    padding: 0;
    list-style: none;
    font-family: "Roboto", sans-serif;
    font-size: 23px;
    line-height: 21.5px;
  }
  .pitch__strong { font-weight: 700; letter-spacing: -0.3px; }
  .pitch__light  { font-weight: 400; }

  .contact {
    position: absolute;
    left: 58px;
    top: 234px;
    font-style: normal;
  }
  .contact__name {
    margin: 0;
    font-family: "Saira", sans-serif;
    font-weight: 300;
    font-size: 26px;
    line-height: 32px;
    white-space: nowrap;
  }
  .contact__cred {
    font-size: 15px;
    margin-left: 8px;
  }
  .contact__phone {
    margin: 0;
    font-family: "Roboto", sans-serif;
    font-size: 19px;
    line-height: 22px;
    letter-spacing: 0.5px;
  }
  .contact__line {
    margin: 0;
    font-family: "Saira", sans-serif;
    font-weight: 400;
    font-size: 19.5px;
    line-height: 22px;
    white-space: nowrap;
  }
  .contact__line--email { margin-top: 4px; }
</style>
</head>
<body>
<main class="sheet">

  <section class="card card--front" aria-label="Business card front">
    <div class="glow glow--front" role="img" aria-label="Blue gradient accent"></div>
    <div class="brand-mark" aria-hidden="true"></div>
    <div class="brand-rule" aria-hidden="true"></div>
    <h1 class="brand-name">tavro capital group llc</h1>
    <p class="role">managing member</p>
  </section>

  <section class="card card--back" aria-label="Business card back">
    <div class="glow glow--back" role="img" aria-label="Blue gradient accent"></div>

    <ul class="pitch">
      <li class="pitch__strong">GAIN FINANCE</li>
      <li class="pitch__light">BIG REWARDS</li>
      <li class="pitch__strong">HIGH RETURNS</li>
      <li class="pitch__light">INVEST IN US</li>
    </ul>

    <address class="contact">
      <p class="contact__name">Delvin Ashcroft<span class="contact__cred">G.E.D.</span></p>
      <p class="contact__phone">555.038.6195</p>
      <p class="contact__line contact__line--email">delvin@tavrocapitalgroup.example</p>
      <p class="contact__line">www.tavrocapitalgroup.example</p>
    </address>
  </section>

</main>
</body>
</html>
```